I need a new business card design for my pharmacy.

I need a business card design. I will include my logo.
The card needs to be readable. I prefer to have my logo on one side along with my website, the other side includes the other information. Please use combination of black, neon green, white, and silver. This needs to catch the eye but yet be clearly visible and legible. Thanks

Industry/Entity Type

Pharmacy

Contact Information for Business Card

It needs to have the following information listed:
Mel's Apothecary Owner/Pharm D.
7134 North Brook Lane
Sioux Falls, SD 57231
Phone 605-318-6207
Fax 605-318-6209
email: mel@melsapothecary-example.com
www.melsapothecary-example.com
Store hours Monday-Friday 8 am- 7 pm
Saturday 8 am- 12 pm
Sunday Closed
Please utilize the colors black, white, and neon green, maybe silver.

Requirements
Must have
• It needs to be easily readable!
Nice to have
• It should catch the eye.
Should not have
• Do not use any other colors except listed: black, neon green, white, & silver.

```html
<!DOCTYPE html>
<html lang="en">
<head>
<meta charset="utf-8">
<title>Mel's Apothecary – Business Card</title>
<link href="https://fonts.googleapis.com/css2?family=Open+Sans:wght@400;600;700&display=swap" rel="stylesheet">
<style>
  :root {
    --neon-green: #a6ce39;
    --ink: #1c1c1c;
    --paper: #ffffff;
    --silver: #c9cbcd;
    --backdrop: #2e3034;
  }
  * { margin: 0; padding: 0; box-sizing: border-box; }
  html, body {
    width: 1200px; height: 864px; overflow: hidden;
    background: var(--backdrop);
    font-family: "Open Sans", Arial, sans-serif;
  }
  .card {
    position: absolute;
    width: 560px; height: 320px;
    background: var(--paper);
    overflow: hidden;
    box-shadow: 0 0 0 1px var(--silver);
  }

  /* Front: brand + store hours */
  .card--front { left: 80px; top: 90px; }
  .front__brand-band {
    position: absolute; left: 0; top: 0; width: 100%; height: 212px;
    background: var(--neon-green);
    display: flex; align-items: center; justify-content: center;
  }
  .front__brand-name {
    color: var(--paper); font-weight: 700; font-size: 44px; letter-spacing: -0.5px;
  }
  .front__hours {
    position: absolute; left: 0; top: 212px; width: 100%; height: 108px;
    text-align: center; color: var(--neon-green);
    padding-top: 18px;
  }
  .hours__title { font-weight: 600; font-size: 17px; letter-spacing: 0.3px; }
  .hours__times { font-size: 14px; margin-top: 6px; }
  .hours__times .divider { margin: 0 8px; }
  .hours__closed { font-weight: 700; font-size: 14px; margin-top: 2px; }

  /* Back: contact details */
  .card--back { left: 560px; top: 474px; }
  .back__brand {
    position: absolute; right: 34px; top: 50px;
    display: flex; align-items: center; gap: 14px;
  }
  .brand__dot { width: 30px; height: 30px; border-radius: 50%; background: var(--neon-green); }
  .brand__rule { width: 1.5px; height: 44px; background: var(--ink); }
  .brand__name { font-weight: 600; font-size: 28px; color: var(--ink); letter-spacing: -0.3px; }

  .back__holder { position: absolute; left: 34px; top: 128px; }
  .holder__name { color: var(--neon-green); font-weight: 600; font-size: 19px; line-height: 1.1; }
  .holder__title { color: var(--ink); font-size: 13px; }

  .back__rule {
    position: absolute; left: 250px; right: 0; top: 160px;
    height: 1px; background: var(--neon-green);
  }

  .back__contact {
    position: absolute; right: 34px; top: 180px;
    list-style: none; text-align: right;
    font-size: 13.5px; color: var(--ink); line-height: 22px;
  }
  .contact__item { display: flex; justify-content: flex-end; align-items: center; gap: 8px; }
  .contact__icon { width: 12px; height: 12px; fill: var(--neon-green); flex: none; }
  .contact__item--address { padding-right: 20px; }
</style>
</head>
<body>

<section class="card card--front" aria-label="Card front">
  <div class="front__brand-band">
    <span class="front__brand-name">Mel's Apothecary</span>
  </div>
  <div class="front__hours">
    <p class="hours__title">STORE HOURS</p>
    <p class="hours__times">Monday-Friday 8 am- 7 pm<span class="divider">|</span>Saturday 8 am- 12 pm</p>
    <p class="hours__closed">Sunday Closed</p>
  </div>
</section>

<section class="card card--back" aria-label="Card back">
  <div class="back__brand">
    <span class="brand__dot"></span>
    <span class="brand__rule"></span>
    <span class="brand__name">Mel's Apothecary</span>
  </div>

  <div class="back__holder">
    <p class="holder__name">Mel's Apothecary</p>
    <p class="holder__title">Owner/Pharm D.</p>
  </div>

  <div class="back__rule"></div>

  <ul class="back__contact">
    <li class="contact__item">605-318-6207
      <svg class="contact__icon" viewBox="0 0 12 12" aria-hidden="true"><path d="M2.4 0.8l1.8 0 0.8 2.6-1.2 1a6 6 0 0 0 3.8 3.8l1-1.2 2.6 0.8v1.8c0 .6-.5 1-1 1A9.6 9.6 0 0 1 1.4 1.8c0-.5.4-1 1-1z"/></svg>
    </li>
    <li class="contact__item">605-318-6209
      <svg class="contact__icon" viewBox="0 0 12 12" aria-hidden="true"><rect x="3" y="0.5" width="6" height="3.5"/><rect x="0.5" y="4.5" width="11" height="5" rx="1"/><rect x="3" y="8" width="6" height="3.5"/></svg>
    </li>
    <li class="contact__item">mel@melsapothecary-example.com
      <svg class="contact__icon" viewBox="0 0 12 12" aria-hidden="true"><path d="M0.5 2.5h11v7h-11z M0.5 2.5l5.5 4 5.5-4" stroke="#fff" stroke-width="0.8"/></svg>
    </li>
    <li class="contact__item">www.melsapothecary-example.com
      <svg class="contact__icon" viewBox="0 0 12 12" aria-hidden="true"><path d="M5 7L7 5M4.5 5.5l-2 2a1.8 1.8 0 0 0 2.5 2.5l2-2M7.5 6.5l2-2A1.8 1.8 0 0 0 7 2l-2 2" fill="none" stroke="#a6ce39" stroke-width="1.3" stroke-linecap="round"/></svg>
    </li>
    <li class="contact__item contact__item--address">7134 North Brook Lane Sioux Falls, SD 57231</li>
  </ul>
</section>

</body>
</html>
```